Boutique Store Selling Antiques and Unique Finds

I need a Web Page designed for my Store Called "Larkmoor Lane". I would like a very classic, muted design that looks European when pulled up. I will be selling Antiques from all over the world and Unique finds that have reproduced. I will also be selling high-end purses and jewelry with unique, reasonable products for the every-day buyer as well.

Target Market(s)

25-70 year old men and women;)

Coding

Coded - Design and coding required

Number of Pages Required

1 page

Colors

Designer to choose only greyscale colors for use in the design.

Requirements
Must have
• I want it

```html
<!DOCTYPE html>
<html lang="en">
<head>
<meta charset="utf-8">
<title>Larkmoor Lane — Antiques &amp; Beautiful Finds</title>
<link rel="stylesheet" href="https://fonts.googleapis.com/css2?family=Roboto+Slab:wght@300;400;700&family=Lora:ital@1&family=Lato:wght@300;400;700&display=swap">
<style>
:root{
  --page:#f2f2f2;
  --ink:#333333;
  --ink-soft:#6b6b6b;
  --muted:#9a9a9a;
  --accent:#7d7d7d;
  --accent-light:#d4d4d4;
  --rule:#cccccc;
  --white:#ffffff;
  --band:#ebebeb;
  --footer:#333333;
  --footer-text:#e6e6e6;
  --footer-brand:#bdbdbd;
}
*{box-sizing:border-box;margin:0;padding:0}
html,body{width:1200px;height:3403px;overflow:hidden}
body{position:relative;background:var(--page);color:var(--ink);font-family:"Lato",sans-serif}
.script{font-family:"Lora",serif;font-style:italic;color:var(--accent)}

/* header */
.brand{position:absolute;left:0;width:1200px;text-align:center;font-family:"Roboto Slab",serif;font-weight:400;color:var(--accent);letter-spacing:5px;text-transform:uppercase}
.site-brand{top:62px;font-size:27px}
.header-icons{position:absolute;top:48px;left:972px;display:flex;gap:22px;align-items:center}
.main-nav{position:absolute;top:130px;left:0;width:1200px}
.main-nav a{font-family:"Roboto Slab",serif;font-size:11px;letter-spacing:.8px;color:var(--ink);text-decoration:none;position:absolute;white-space:nowrap}
.main-nav a.active{color:var(--accent)}
.nav-underline{position:absolute;top:155px;left:226px;width:46px;height:1px;background:var(--accent)}

/* hero */
.hero{position:absolute;left:11px;top:172px;width:1174px;height:481px;background:linear-gradient(180deg,#4a4a4a 0%,#383838 12%,#c8c8c8 30%,#e8e8e8 60%,#9e9e9e 88%,#6a6a6a 100%)}
.hero-photo{position:absolute;left:200px;top:70px;width:420px;height:411px;background:radial-gradient(ellipse at 50% 45%,#8e8e8e 0%,#5e5e5e 45%,rgba(90,90,90,0) 72%)}
.hero-copy{position:absolute;right:84px;top:212px;text-align:right;font-family:"Roboto Slab",serif;font-weight:300;font-size:31px;line-height:44px;letter-spacing:.5px}
.hero-copy .g{color:var(--accent)}
.hero-copy b{font-weight:700}
.arrow{position:absolute}

/* section heads */
.section-head{position:absolute;left:0;width:1200px;text-align:center}
.section-head .script{font-size:17px;display:block}
.section-head h2{font-family:"Roboto Slab",serif;font-weight:300;font-size:31px;letter-spacing:2.5px;color:var(--ink);margin-top:6px}
.rule{position:absolute;height:1px;background:var(--rule)}

/* collection cards */
.card{position:absolute;top:843px;width:222px}
.card-photo{width:222px;height:349px}
.card-label{position:absolute;left:13px;top:283px;width:196px;height:66px;background:var(--white);text-align:center;padding-top:14px}
.card-label .script{font-size:13px;display:block}
.card-label .name{font-family:"Roboto Slab",serif;font-weight:300;font-size:16px;letter-spacing:.6px;margin-top:4px;display:block}
.card-text{font-weight:300;font-size:12px;line-height:23px;color:var(--ink-soft);margin-top:20px}
.view-more{position:absolute;top:440px;left:38px;font-size:11px;font-weight:700;letter-spacing:1px;color:var(--ink-soft);display:flex;align-items:center;gap:16px}
.view-more::before{content:"";display:block;width:28px;height:1px;background:var(--muted)}

/* sale banner */
.sale{position:absolute;left:116px;top:1442px;width:966px;height:465px;background:linear-gradient(120deg,#474747 0%,#666666 35%,#525252 60%,#3b3b3b 100%);color:var(--white);text-align:center}
.sale .script{position:absolute;left:0;width:966px;top:138px;font-size:22px;color:var(--accent-light)}
.sale h3{position:absolute;left:0;width:966px;top:170px;font-family:"Roboto Slab",serif;font-weight:300;font-size:42px;letter-spacing:1.5px}
.sale p{position:absolute;left:0;width:966px;top:228px;font-size:12px;line-height:21px}
.btn{position:absolute;font-family:"Roboto Slab",serif;font-size:11px;font-weight:700;letter-spacing:.5px;text-align:center}
.sale .btn{left:442px;top:296px;width:109px;height:38px;line-height:37px;border:1px solid var(--white);color:var(--white)}

/* products */
.product{position:absolute;top:2173px;width:313px;text-align:center}
.product-photo{width:313px;height:416px}
.product .title{font-family:"Roboto Slab",serif;font-weight:300;font-size:16px;margin-top:28px}
.product .price{font-family:"Roboto Slab",serif;font-size:15px;color:var(--accent);margin-top:6px}
.dot{position:absolute;top:2705px;width:4px;height:4px;border-radius:50%;background:#b8b8b8}
.dot.on{background:var(--ink-soft);width:5px;height:5px;top:2704px}
.view-all{left:544px;top:2749px;width:110px;height:39px;line-height:38px;border:1px solid var(--accent);color:var(--ink);background:var(--white)}

/* newsletter */
.newsletter{position:absolute;left:0;top:2844px;width:1200px;height:223px;background:var(--band);text-align:center}
.newsletter h4{font-weight:700;font-size:25px;letter-spacing:-.3px;margin-top:46px}
.newsletter p{font-size:12px;color:var(--ink-soft);margin-top:16px;font-weight:300}
.email-field{position:absolute;left:439px;top:145px;width:308px;height:32px;background:var(--white);text-align:left;font-size:9px;color:var(--muted);padding:11px 0 0 21px}

/* footer */
.site-footer{position:absolute;left:0;top:3067px;width:1200px;height:336px;background:var(--footer);color:var(--footer-text);font-family:"Roboto Slab",serif}
.footer-brand{top:91px;font-size:27px;color:var(--footer-brand)}
.contact{position:absolute;left:118px;top:158px;font-size:12px;line-height:32px;letter-spacing:.3px}
.footer-links{position:absolute;top:158px;font-size:11px;line-height:26.5px;letter-spacing:.4px;list-style:none}
.follow{position:absolute;left:867px;top:158px;font-size:12px;font-weight:700;letter-spacing:.3px}
.socials{position:absolute;left:866px;top:188px;display:flex;gap:8px}
.socials span{width:27px;height:27px;border:1px solid var(--footer-text);border-radius:50%;display:block}
.to-top{position:absolute;left:1142px;top:275px;width:40px;height:40px;background:#474747}
</style>
</head>
<body>

<header>
  <div class="brand site-brand">Larkmoor Lane</div>
  <div class="header-icons">
    <svg width="16" height="16" viewBox="0 0 16 16" fill="none" stroke="#555" stroke-width="1.2"><rect x="2.5" y="5.5" width="10" height="9"/><path d="M5 5.5V4a2.5 2.5 0 0 1 5 0v1.5"/></svg>
    <svg width="16" height="16" viewBox="0 0 16 16" fill="none" stroke="#555" stroke-width="1.3"><circle cx="6.5" cy="6.5" r="4.5"/><path d="M10 10l4 4"/></svg>
    <svg width="24" height="10" viewBox="0 0 24 10" stroke="#555" stroke-width="1.2"><path d="M1 2h22M1 8h22"/></svg>
  </div>
  <nav class="main-nav">
    <a class="active" href="#" style="left:232px">HOME</a>
    <a href="#" style="left:320px">ANTIQUE &amp; VINTAGE</a>
    <a href="#" style="left:491px">ANTIQUE JEWELLERY</a>
    <a href="#" style="left:669px">ART</a>
    <a href="#" style="left:739px">FURNISHING</a>
    <a href="#" style="left:853px">OTHERS</a>
    <a href="#" style="left:947px">SALE</a>
  </nav>
  <div class="nav-underline"></div>
</header>

<section class="hero">
  <div class="hero-photo" role="img" aria-label="Antique crown set with stones on a pedestal, beneath a carved frame"></div>
  <div class="hero-copy">
    <div class="g">ANTIQUES <b style="color:var(--ink)">&amp;</b> BEAUTIFUL FINDS</div>
    <div>FROM AROUND THE <b class="g">WORLD</b></div>
  </div>
  <svg class="arrow" style="left:46px;top:236px" width="14" height="32" viewBox="0 0 14 32" fill="none" stroke="#333" stroke-width="1.5"><path d="M13 1L1 16l12 15"/></svg>
  <svg class="arrow" style="left:1120px;top:236px" width="14" height="32" viewBox="0 0 14 32" fill="none" stroke="#333" stroke-width="1.5"><path d="M1 1l12 15L1 31"/></svg>
</section>

<div class="section-head" style="top:736px">
  <span class="script">Unique &amp; Memorable</span>
  <h2>OUR COLLECTION</h2>
</div>
<div class="rule" style="left:313px;top:787px;width:87px"></div>
<div class="rule" style="left:800px;top:787px;width:88px"></div>

<article class="card" style="left:116px">
  <div class="card-photo" role="img" aria-label="Wood-panelled hallway with staircase and crystal chandelier" style="background:linear-gradient(160deg,#7a7a7a 0%,#4a4a4a 50%,#2e2e2e 100%)"></div>
  <div class="card-label"><span class="script">Collection</span><span class="name">ANTIQUE &amp; VINTAGE</span></div>
  <p class="card-text">Lorem ipsum dolor sit amet eiusmod, consectetur adip isi cing elit, sed do.</p>
  <div class="view-more">View more</div>
</article>
<article class="card" style="left:365px">
  <div class="card-photo" role="img" aria-label="Wire sculpture on a pale surface" style="background:linear-gradient(180deg,#d6d6d6 0%,#c0c0c0 55%,#989898 100%)"></div>
  <div class="card-label"><span class="script">Collection</span><span class="name">ART &amp; DECORATION</span></div>
  <p class="card-text">Lorem ipsum dolor sit amet eiusmod, consectetur adip isi cing elit, sed do.</p>
  <div class="view-more">View more</div>
</article>
<article class="card" style="left:613px">
  <div class="card-photo" role="img" aria-label="Framed tapestry above a dark wooden chest with a potted plant" style="background:linear-gradient(180deg,#8c8c8c 0%,#6c6c6c 45%,#303030 100%)"></div>
  <div class="card-label"><span class="script">Collection</span><span class="name">FURNISHING</span></div>
  <p class="card-text">Lorem ipsum dolor sit amet eiusmod, consectetur adip isi cing elit, sed do.</p>
  <div class="view-more">View more</div>
</article>
<article class="card" style="left:860px">
  <div class="card-photo" role="img" aria-label="Jewelled silver crown on a stand" style="background:linear-gradient(180deg,#c8c8c8 0%,#6a6a6a 45%,#4a4a4a 100%)"></div>
  <div class="card-label"><span class="script">Collection</span><span class="name">JEWELLERY</span></div>
  <p class="card-text">Lorem ipsum dolor sit amet eiusmod, consectetur adip isi cing elit, sed do.</p>
  <div class="view-more">View more</div>
</article>

<section class="sale" role="img" aria-label="Shelves of ribbon rolls, trims and fabric bolts">
  <span class="script">Larkmoor Lane</span>
  <h3>COLLECTION SALE</h3>
  <p>Lorem ipsum dolor sit amet, consectetur adipisicing elit, sed do eius<br>mod tempor incididunt ut labore et dolore magna aliqua.</p>
  <div class="btn">SHOP NOW</div>
</section>

<div class="section-head" style="top:2039px">
  <span class="script">Our Latest Collection</span>
  <h2>NEW ARRIVALS</h2>
</div>
<div class="rule" style="left:333px;top:2090px;width:87px"></div>
<div class="rule" style="left:781px;top:2090px;width:87px"></div>

<svg class="arrow" style="left:52px;top:2385px" width="10" height="24" viewBox="0 0 10 24" fill="none" stroke="#555" stroke-width="1.3"><path d="M9 1L1 12l8 11"/></svg>
<svg class="arrow" style="left:1125px;top:2385px" width="10" height="24" viewBox="0 0 10 24" fill="none" stroke="#555" stroke-width="1.3"><path d="M1 1l8 11-8 11"/></svg>

<article class="product" style="left:108px">
  <div class="product-photo" role="img" aria-label="Fur-trimmed crown resting on a stack of books" style="background:linear-gradient(180deg,#d6d6d6 0%,#bdbdbd 40%,#4e4e4e 65%,#333333 100%)"></div>
  <div class="title">Antique Item</div>
  <div class="price">$800.00</div>
</article>
<article class="product" style="left:440px">
  <div class="product-photo" role="img" aria-label="Star crown on leather-bound books" style="background:linear-gradient(180deg,#cfcfcf 0%,#8e8e8e 45%,#565656 75%,#3a3a3a 100%)"></div>
  <div class="title">Antique Item</div>
  <div class="price">$1085.00</div>
</article>
<article class="product" style="left:769px">
  <div class="product-photo" role="img" aria-label="Embroidered insignia patch on marble" style="background:radial-gradient(ellipse at 50% 55%,#404040 0%,#262626 32%,#d4d4d4 52%,#e2e2e2 100%)"></div>
  <div class="title">Antique Item</div>
  <div class="price">$568.00</div>
</article>

<span class="dot" style="left:569px"></span>
<span class="dot on" style="left:598px"></span>
<span class="dot" style="left:627px"></span>
<div class="btn view-all">VIEW MORE</div>

<section class="newsletter">
  <h4>JOIN EMAIL</h4>
  <p>Sign up to receive the latest news and updates</p>
  <div class="email-field">Your email address
    <svg style="position:absolute;right:16px;top:9px" width="8" height="14" viewBox="0 0 8 14" fill="none" stroke="#333" stroke-width="1.4"><path d="M1 1l6 6-6 6"/></svg>
  </div>
</section>

<footer class="site-footer">
  <div class="brand footer-brand">Larkmoor Lane</div>
  <div class="contact">
    418 Harrowgate Row Wendlebury<br>
    555-014-2287, 555-019-4630<br>
    hello@larkmoorlane.com<br>
    Copyright © Fernhill Studio 2019
  </div>
  <ul class="footer-links" style="left:435px">
    <li>Antique &amp; Vintage</li><li>Jewellery</li><li>Art</li><li>Furnishing</li><li>Others</li>
  </ul>
  <ul class="footer-links" style="left:637px">
    <li>Terms &amp; Conditions</li><li>Privacy Policy</li><li>Refund Policy</li><li>My Account</li>
  </ul>
  <div class="follow">Follow Us At:</div>
  <div class="socials"><span></span><span></span><span></span><span></span><span></span></div>
  <div class="to-top">
    <svg style="position:absolute;left:14px;top:16px" width="12" height="7" viewBox="0 0 12 7" fill="none" stroke="#ddd" stroke-width="1.2"><path d="M1 6l5-5 5 5"/></svg>
  </div>
</footer>

</body>
</html>
```